Kelderby Farm

Need a nice simple clean double sided business card that has our logo and info on:
Kelder By Farm
Martin & Lydia Okerlund
kelderbyfarm@examplemail.test
Martin: 1-555-218-4391
Lydia: 1-555-903-2657
Instagram @ kelderby_farm

Contact Information for Business Card

Martin & Lydia Okerlund kelderbyfarm@examplemail.test Martin: 1-555-218-4391 Lydia: 1-555-903-2657

```html
<!DOCTYPE html>
<html lang="en">
<head>
<meta charset="utf-8">
<title>Kelder By Farm – Business Card</title>
<link href="https://fonts.googleapis.com/css2?family=Roboto:wght@400;500;700&display=swap" rel="stylesheet">
<style>
  :root {
    --farm-green: #67a042;
    --harvest-orange: #f7a11a;
    --ink-grey: #4a4a4a;
    --card-white: #ffffff;
    --backdrop: #2b2b2b;
  }
  * { box-sizing: border-box; margin: 0; padding: 0; }
  html, body { width: 1200px; height: 900px; overflow: hidden; }
  body {
    background: var(--backdrop);
    font-family: "Roboto", sans-serif;
    display: flex;
    flex-direction: column;
    align-items: center;
    justify-content: center;
    gap: 40px;
  }
  .card {
    position: relative;
    width: 700px;
    height: 400px;
    overflow: hidden;
    box-shadow: 0 10px 30px rgba(0,0,0,0.45);
  }
  .card-front { background: var(--card-white); }
  .card-back { background: var(--farm-green); display: flex; align-items: center; justify-content: center; }

  .front-swoop { position: absolute; inset: 0; width: 100%; height: 100%; }

  .brand-lockup {
    position: absolute;
    left: 60px;
    top: 48px;
    width: 260px;
    display: flex;
    flex-direction: column;
    align-items: center;
    gap: 12px;
  }
  .brand-circle {
    width: 104px; height: 104px;
    border-radius: 50%;
    border: 4px solid var(--farm-green);
  }
  .brand-name {
    font-weight: 500;
    font-size: 28px;
    letter-spacing: 1px;
    text-transform: uppercase;
    color: var(--farm-green);
    white-space: nowrap;
  }

  .divider {
    position: absolute;
    left: 345px;
    top: 100px;
    width: 2px;
    height: 165px;
    background: var(--farm-green);
  }

  .contact-block {
    position: absolute;
    left: 370px;
    top: 104px;
  }
  .contact-names {
    font-weight: 700;
    font-size: 22px;
    color: var(--farm-green);
    margin-bottom: 12px;
    white-space: nowrap;
  }
  .contact-line {
    display: flex;
    align-items: center;
    gap: 8px;
    font-size: 16px;
    color: var(--ink-grey);
    line-height: 26px;
    white-space: nowrap;
  }
  .contact-line .owner { color: var(--farm-green); font-weight: 500; }
  .contact-icon { width: 16px; height: 16px; flex: none; }
  .social-square {
    width: 13px; height: 13px;
    border: 2px solid var(--harvest-orange);
    border-radius: 3px;
    margin: 0 1.5px;
    flex: none;
  }

  .back-lockup {
    display: flex;
    flex-direction: column;
    align-items: center;
    gap: 18px;
  }
  .back-lockup .brand-circle { width: 130px; height: 130px; border-color: var(--card-white); }
  .back-lockup .brand-name { color: var(--card-white); font-size: 40px; }
</style>
</head>
<body>

  <section class="card card-front" aria-label="Business card front">
    <svg class="front-swoop" viewBox="0 0 700 400" preserveAspectRatio="none" aria-hidden="true">
      <path class="swoop-orange" d="M0,228 C140,320 400,368 700,366 L700,400 L0,400 Z" fill="var(--harvest-orange)"/>
      <path class="swoop-white" d="M0,237 C140,329 400,377 700,375 L700,400 L0,400 Z" fill="var(--card-white)"/>
      <path class="swoop-green" d="M0,244 C140,336 400,384 700,382 L700,400 L0,400 Z" fill="var(--farm-green)"/>
    </svg>

    <div class="brand-lockup">
      <div class="brand-circle"></div>
      <div class="brand-name">Kelder By Farm</div>
    </div>

    <div class="divider"></div>

    <div class="contact-block">
      <p class="contact-names">Martin &amp; Lydia Okerlund</p>
      <p class="contact-line">
        <svg class="contact-icon" viewBox="0 0 24 24" aria-hidden="true"><path d="M6.6 10.8a15 15 0 0 0 6.6 6.6l2.2-2.2a1 1 0 0 1 1-.25 11.4 11.4 0 0 0 3.6.57 1 1 0 0 1 1 1V20a1 1 0 0 1-1 1A17 17 0 0 1 3 4a1 1 0 0 1 1-1h3.5a1 1 0 0 1 1 1c0 1.25.2 2.45.57 3.57a1 1 0 0 1-.25 1z" fill="var(--harvest-orange)"/></svg>
        1-555-218-4391 <span class="owner">Martin</span>
      </p>
      <p class="contact-line">
        <svg class="contact-icon" viewBox="0 0 24 24" aria-hidden="true"><path d="M6.6 10.8a15 15 0 0 0 6.6 6.6l2.2-2.2a1 1 0 0 1 1-.25 11.4 11.4 0 0 0 3.6.57 1 1 0 0 1 1 1V20a1 1 0 0 1-1 1A17 17 0 0 1 3 4a1 1 0 0 1 1-1h3.5a1 1 0 0 1 1 1c0 1.25.2 2.45.57 3.57a1 1 0 0 1-.25 1z" fill="var(--harvest-orange)"/></svg>
        1-555-903-2657 <span class="owner">Lydia</span>
      </p>
      <p class="contact-line">
        <svg class="contact-icon" viewBox="0 0 24 24" aria-hidden="true"><path d="M2 5h20v14H2z" fill="var(--harvest-orange)"/><path d="M2 5l10 8 10-8" fill="none" stroke="var(--card-white)" stroke-width="2"/></svg>
        kelderbyfarm@examplemail.test
      </p>
      <p class="contact-line">
        <span class="social-square"></span>
        @ kelderby_farm
      </p>
    </div>
  </section>

  <section class="card card-back" aria-label="Business card back">
    <div class="back-lockup">
      <div class="brand-circle"></div>
      <div class="brand-name">Kelder By Farm</div>
    </div>
  </section>

</body>
</html>
```